Wine Bottle Label Logo Design

My fiancé and I are getting married in September and we made homemade wine which will be given to the guests as a wedding favor. We need label/logo for our wine bottles. We were looking for something rustic yet modern and simple. We had an idea for beige and cranberry colored wine stained, weathered, imperfect heart. Things that will need to be incorporated into the label design are as follows:
Our last name and also the name of the wine: Bastoni
The year: 2012
Where is says Alcohol Content on a wine bottle normally write: Alcohol: Deceiving% by vol.
Type of wine: Red Wine
Incorporate our wedding date: Foot Stomped and Bottled for Jess and Ned's Wedding Day 9/28/13

```html
<!DOCTYPE html>
<html lang="en">
<head>
<meta charset="utf-8">
<title>Bastoni 2012 Red Wine Label</title>
<link rel="stylesheet" href="https://fonts.googleapis.com/css2?family=Old+Standard+TT:ital,wght@0,400;0,700;1,400&family=Dancing+Script:wght@500&display=swap">
<style>
  :root {
    --backdrop: #f6efe4;
    --paper: #f3f0ea;
    --paper-edge: #e4dfd4;
    --ink: #1d1b1a;
    --cranberry: #9c1a2b;
    --cranberry-soft: #c2475a;
    --stitch: #cfc8bb;
  }
  * { box-sizing: border-box; margin: 0; padding: 0; }
  html, body {
    width: 960px;
    height: 1200px;
    overflow: hidden;
    background: var(--backdrop);
  }
  .label {
    position: absolute;
    left: 200px;
    top: 60px;
    width: 560px;
    height: 1080px;
    background: radial-gradient(ellipse at 50% 40%, #f8f6f1 0%, var(--paper) 60%, var(--paper-edge) 100%);
    box-shadow: 0 2px 6px rgba(0,0,0,0.12);
    text-align: center;
    color: var(--ink);
  }
  .label__frame {
    position: absolute;
    inset: 9px;
    border: 2px dotted var(--stitch);
    pointer-events: none;
  }
  .label__name {
    position: absolute;
    top: 100px;
    left: 0;
    right: 0;
    font-family: "Old Standard TT", serif;
    font-weight: 700;
    font-size: 98px;
    letter-spacing: 1px;
    line-height: 1;
  }
  .label__vintage {
    position: absolute;
    top: 244px;
    left: 0;
    right: 0;
    font-family: "Old Standard TT", serif;
    font-weight: 700;
    font-size: 60px;
    line-height: 1;
  }
  .label__heart {
    position: absolute;
    left: 109px;
    top: 362px;
    width: 382px;
    height: 356px;
    border-radius: 50% 50% 46% 46%;
    background: radial-gradient(circle at 50% 50%, rgba(194,71,90,0.10) 0%, rgba(156,26,43,0.28) 70%, rgba(156,26,43,0) 72%);
  }
  .label__type {
    position: absolute;
    top: 790px;
    left: 0;
    right: 0;
    font-family: "Dancing Script", cursive;
    font-weight: 500;
    font-size: 52px;
    color: var(--cranberry);
    line-height: 1;
  }
  .label__dedication {
    position: absolute;
    top: 928px;
    left: 0;
    right: 0;
    font-family: "Old Standard TT", serif;
    font-size: 22px;
    line-height: 31px;
  }
  .label__alcohol {
    position: absolute;
    top: 1025px;
    left: 0;
    right: 0;
    font-family: "Dancing Script", cursive;
    font-size: 17px;
    color: #444;
  }
</style>
</head>
<body>
  <main class="label">
    <div class="label__frame"></div>
    <h1 class="label__name">BASTONI</h1>
    <p class="label__vintage">2012</p>
    <div class="label__heart" role="img" aria-label="Hand-painted cranberry wine-stained, weathered heart outline"></div>
    <p class="label__type">Red Wine</p>
    <p class="label__dedication">Foot Stomped and Bottled for<br>Jess and Ned's Wedding Day 9/28/13</p>
    <p class="label__alcohol">Alcohol: Deceiving % by vol.</p>
  </main>
</body>
</html>
```